Business Card for Tutoring Company

We need a logo/symbol for an education company, along with an attractive business card. The logo should resemble both a pi symbol and the letter T.

Dear Designers,

I am narrowing down what I am looking for. 
I want the front of the card to be primarily white, with the company name "Maple Grove Learning" positioned towards the center.  The first letter, 'T' in 'Maple' will be modified so that it resembles a Pi symbol.
My personal information will be at the bottom.  If you think it fits, the website can be strewn across the top.

As for the back of the card, it will be primarily blue.  Toward the center will be the same T/pi shape engraved into a circular disk/button/emblem shape with some border.  It should be noted that I do like shiny blue, like the blue face of a Vantor.  Underneath the logo will be white text that reads, "Making Independent Learners and Thinkers."  At the very bottom of the card in smaller white font, the website "MapleGroveLearning.com" is written.

For more clarification, see my recent attachment.

Thank you.

Winston

Industry/Entity Type

Education

Logo styles of interest
Pictorial/Combination Logo
Requirements
Must have
• LOGO:
The logo is a solid blue circle with a symbol cutout from it. The cut out should closely resemble π and be the color white.

CARD:
The front has the logo in the top left corner, with "MAPLE GROVE LEARNING" written out beside it, spanning the width of the card. " At the bottom, personal information can be placed: Name, Title, Phone, Email.
The back has the the logo centered and enlarged. The website is printed "MapleGroveLearning.com
Nice to have
• LOGO:
It would be nice if the logo/pi symbol could be used as a letter T when spelling MGL or Maple Grove Learning.

CARD:
The enlarged logo on the back of the card can be enhanced (i.e. the blue is not solid blue but shiny, like the metallic blue face of a vantor) It would also be nice if the logo had a cool background (i.e. instead of the cutout of the pi-shape being white, it could be outerspace or something. Also, a motto "Making Independent Learner and Thinkers" printed under "MapleGroveLearning.com" would be nice, if it fits.

```html
<!DOCTYPE html>
<html lang="en">
<head>
<meta charset="utf-8">
<title>Maple Grove Learning – Business Card</title>
<link rel="stylesheet" href="https://fonts.googleapis.com/css2?family=Open+Sans:ital,wght@0,400;0,600;0,700;1,400;1,700&display=swap">
<style>
  :root {
    --navy: #0b3362;
    --navy-deep: #072548;
    --navy-light: #17497f;
    --emblem: #1d3f6e;
    --white: #ffffff;
    --paper: #ffffff;
    --backdrop: #e4e6e9;
    --rule: #0b3362;
  }
  * { margin: 0; padding: 0; box-sizing: border-box; }
  html, body {
    width: 1200px;
    height: 900px;
    overflow: hidden;
    background: var(--backdrop);
    font-family: "Open Sans", Arial, sans-serif;
  }
  .canvas {
    position: relative;
    width: 1200px;
    height: 900px;
  }
  .card {
    position: absolute;
    width: 560px;
    height: 320px;
    border-radius: 4px;
    overflow: hidden;
    box-shadow: 0 6px 18px rgba(0, 0, 0, 0.18);
  }

  /* Back of card */
  .card-back {
    left: 70px;
    top: 90px;
    background: linear-gradient(160deg, var(--navy-light) 0%, var(--navy) 45%, var(--navy-deep) 100%);
    color: var(--white);
    text-align: center;
  }
  .card-back .sheen {
    position: absolute;
    inset: 0;
    width: 100%;
    height: 100%;
  }
  .emblem {
    position: absolute;
    left: 50%;
    top: 34px;
    width: 130px;
    height: 130px;
    margin-left: -65px;
    border-radius: 50%;
    border: 4px solid var(--white);
    background: var(--emblem);
  }
  .back-name {
    position: absolute;
    left: 0;
    right: 0;
    top: 180px;
    font-size: 15px;
    font-weight: 600;
    letter-spacing: 2px;
  }
  .tagline {
    position: absolute;
    left: 0;
    right: 0;
    top: 210px;
    font-size: 23px;
    font-weight: 400;
    letter-spacing: 1px;
  }
  .website {
    position: absolute;
    left: 0;
    right: 0;
    bottom: 24px;
    font-size: 17px;
    letter-spacing: 1px;
  }

  /* Front of card */
  .card-front {
    left: 570px;
    top: 490px;
    background: var(--paper);
  }
  .top-band {
    position: absolute;
    left: 0; right: 0; top: 0;
    height: 34px;
    background: var(--navy);
  }
  .wordmark {
    position: absolute;
    left: 0; right: 0;
    top: 52px;
    text-align: center;
    color: var(--navy);
    font-weight: 700;
    line-height: 1;
  }
  .wordmark-main {
    display: block;
    font-size: 84px;
    letter-spacing: 2px;
  }
  .wordmark-sub {
    display: block;
    margin-top: 6px;
    font-size: 25px;
    letter-spacing: 1.5px;
  }
  .divider {
    position: absolute;
    left: 0; right: 0;
    top: 222px;
    height: 3px;
    background: var(--rule);
  }
  .contact-band {
    position: absolute;
    left: 0; right: 0; bottom: 0;
    height: 88px;
    background: var(--navy);
    color: var(--white);
  }
  .person {
    position: absolute;
    left: 48px;
    top: 14px;
  }
  .person-name {
    font-size: 19px;
    font-weight: 700;
    font-style: italic;
    letter-spacing: 0.5px;
  }
  .person-title {
    font-size: 13px;
    font-style: italic;
  }
  .details {
    position: absolute;
    left: 330px;
    top: 24px;
    font-size: 14px;
    font-style: italic;
    line-height: 1.7;
  }
</style>
</head>
<body>
<main class="canvas">

  <section class="card card-back" aria-label="Back of business card">
    <svg class="sheen" viewBox="0 0 560 320" aria-hidden="true">
      <path d="M0 250 C 150 120, 360 40, 560 20 L560 0 L0 0 Z" fill="#ffffff" opacity="0.05"/>
      <path d="M0 320 C 120 200, 330 110, 560 80" fill="none" stroke="#ffffff" stroke-opacity="0.12" stroke-width="2"/>
    </svg>
    <div class="emblem" aria-hidden="true"></div>
    <p class="back-name">MAPLE GROVE LEARNING</p>
    <p class="tagline">Building Curious Minds</p>
    <p class="website">MapleGroveLearning.com</p>
  </section>

  <section class="card card-front" aria-label="Front of business card">
    <div class="top-band"></div>
    <h1 class="wordmark">
      <span class="wordmark-main">MAPLE</span>
      <span class="wordmark-sub">GROVE LEARNING</span>
    </h1>
    <div class="divider"></div>
    <div class="contact-band">
      <div class="person">
        <p class="person-name">WINSTON HALE</p>
        <p class="person-title">Education Consultant</p>
      </div>
      <div class="details">
        <p class="phone">(555) 014 2287</p>
        <p class="email">winston@MGLbest.com</p>
      </div>
    </div>
  </section>

</main>
</body>
</html>
```